Patient Recruitment Presentation for a Clinical Trial

We need a powerpoint designed to recruit patients for a clinical trial. We need 4 slides designed: an opening slide, two body slides, and an end slide. The opening slide should include the question, "Do you suffer from Depression?" in the middle of the screen, but other than that just include the design, graphic, or texture that you develop. The 2 body slides should allow for the title of study (please use “Depression Research Study”) to be across the top and contact information (phone number, URL) to be on the bottom of the slide, either centered or left or right justified. Whether this text (study title and contact information) is set off by a banner or shape that stretches across the entire slide or just provides a background to that text is up to you. One of the two body slides should include the attached horizontal stock image with a clear section to insert text either beside or over the top of the negative space of the image. This image should be stretch to the full width of the screen. The second body slide should include the attached vertical stock image, with a clear section to insert text beside the picture. (You can crop vertical portions of the images if needed.)

The end slide should resemble the opening slide in terms of design, yet this time includes the study title and contact information prominently displayed.

In terms of design, we’re looking for something clean and trustworthy, and even though this is medical, we don’t want any pills, test tubes, or heart rate lines. We’re trying to give people hope, so we want to earn their trust by communicating quality and excellence.

Please see the attached examples of the types of designs and layouts we like, how the images need to be treated, and places for text need to be designed.

We need the design to be 1920x1080 pixels, and we need the slides delivered as layered PSD files so we can manipulate as needed.

Thanks!

Target Market(s)

Adults in the US that are not working full time and able to participate in a research study.

Industry/Entity Type

Medical

Font styles to use
Serif
Sans Serif

Requirements
Must have
• The design must use the two images attached as specified in the brief. Other than that, I'm open to your creative interpretation.
Nice to have
• Nice clean design, clean fonts, nice color palette.
Should not have
• Images or designs relating to the medical world, no test tubes, heart rate lines, images of doctors or pills, etc.

```html
<!DOCTYPE html>
<html lang="en">
<head>
<meta charset="utf-8">
<title>Depression Research Study – Opening Slide</title>
<link rel="stylesheet" href="https://fonts.googleapis.com/css2?family=Source+Sans+3:wght@400&display=swap">
<style>
  :root {
    --navy: #05517f;
    --sky: #0089b5;
    --white: #ffffff;
  }
  html, body {
    margin: 0;
    padding: 0;
    width: 1200px;
    height: 675px;
    overflow: hidden;
    background: var(--navy);
  }
  .slide {
    position: relative;
    width: 1200px;
    height: 675px;
    background: var(--navy);
    overflow: hidden;
  }
  .question-mark {
    position: absolute;
    left: 0;
    top: 0;
    width: 1200px;
    height: 675px;
  }
  .question-band {
    position: absolute;
    left: 0;
    top: 278px;
    width: 1200px;
    height: 127px;
    background: var(--sky);
    display: flex;
    align-items: center;
    justify-content: center;
  }
  .question-text {
    margin: 0;
    color: var(--white);
    font-family: "Source Sans 3", "Myriad Pro", sans-serif;
    font-weight: 400;
    font-size: 94px;
    letter-spacing: -1.5px;
    line-height: 1;
    white-space: nowrap;
    transform: translateY(-4px);
  }
</style>
</head>
<body>
  <main class="slide">
    <svg class="question-mark" viewBox="0 0 1200 675" aria-hidden="true">
      <path fill="var(--sky)" d="
        M422 40
        L422 160 L484 160 L484 90
        C540 76 600 72 650 80
        C700 90 722 120 722 160
        C722 210 690 245 640 285
        C575 335 540 380 540 430
        L540 478 L624 478 L624 440
        C624 380 660 340 720 295
        C780 250 812 210 812 155
        C812 60 730 15 610 15
        C540 15 480 24 422 40 Z" />
      <rect fill="var(--sky)" x="530" y="562" width="104" height="94" />
    </svg>
    <section class="question-band">
      <h1 class="question-text">Lorem ipsum dolor sit amet?</h1>
    </section>
  </main>
</body>
</html>
```